"Mug Rover" Wordpress Design Project

Mugrover.example is the one-stop destination for maps and reviews of coffee shops and cafes in Minneapolis. We thoroughly compile information for all cafes in the area, and then plot them on a map for customers. The site helps people who want to visit new, different, or more conveniently-located coffee shops, while boosting visibility for the shops themselves.

We would like to see designs that are simple as well as eye-catching. The final design will reflect Mug Rover's convenient, personable function (as well as its focus on giving directions to people).

It must work with Pel Kits framework (see pelkits.example). Each review page will include a map to the location, photos of the cafe, a written review, comments by users and a user rating system (i.e. 1 to 5 stars).

Target Market(s)

Coffee connoisseurs, students, scenesters, people that work from computers

Industry/Entity Type

Cafe

Requirements
Must have
• This wordpress theme MUST work with Pel Kits and provide a URL for the pel kits framework (pelkits.example.

```html
<!DOCTYPE html>
<html lang="en">
<head>
<meta charset="utf-8">
<title>Mug Rover</title>
<link rel="stylesheet" href="https://fonts.googleapis.com/css2?family=Crimson+Text:wght@400;600&family=Noto+Sans:ital,wght@0,400;0,700;1,400&display=swap">
<style>
:root{
  --bean-dark:#5a3a22;
  --bean-mid:#a9764c;
  --bean-light:#d4ab84;
  --red:#b3141a;
  --red-dark:#7c0c10;
  --link:#c0151b;
  --visited:#b04a4a;
  --ink:#222;
  --muted:#555;
  --panel:#f4f4f4;
  --header:#f3f3f3;
  --rule:#c9c9c9;
}
*{box-sizing:border-box;margin:0;padding:0}
html,body{width:1200px;height:600px;overflow:hidden}
body{position:relative;font-family:"Noto Sans",sans-serif;color:var(--ink);font-size:10.5px;line-height:1.2;
  background:radial-gradient(circle at 30% 60%,var(--bean-light),var(--bean-mid) 55%,var(--bean-dark));}
.top-strip{position:absolute;left:0;top:0;width:1200px;height:25px;
  background:linear-gradient(90deg,var(--bean-mid),var(--bean-light),var(--bean-mid),var(--bean-light),var(--bean-mid))}
.bean-backdrop{position:absolute;left:0;top:215px;width:1200px;height:385px;
  background:radial-gradient(ellipse at 15% 40%,#e2c3a2,#b98a60 40%,#8d5f3c 80%),var(--bean-mid);opacity:.9}
.main-nav{position:absolute;left:272px;top:5px;display:flex;gap:5px}
.main-nav a{display:block;height:20px;padding:0 16px;line-height:20px;color:#fff;text-decoration:none;font-size:10.5px;
  background:linear-gradient(#c71b21,var(--red-dark));border:1px solid #5e0a0d;border-bottom:none;border-radius:3px 3px 0 0}
.site-header{position:absolute;left:0;top:25px;width:1200px;height:190px;background:var(--header)}
.brand{position:absolute;left:460px;top:66px;display:flex;align-items:center;gap:18px}
.brand-dot{width:70px;height:70px;border-radius:50%;background:var(--red)}
.brand-name{font-family:"Noto Sans",sans-serif;font-weight:700;font-size:44px;color:var(--bean-dark);letter-spacing:-1px}
.page{position:absolute;left:263px;top:200px;width:680px;height:420px;background:var(--panel);
  border:2px solid #8a8a8a;border-radius:10px 10px 0 0;box-shadow:0 0 6px rgba(0,0,0,.4)}
.sidebar{position:absolute;left:14px;top:16px;width:138px}
.widget-title{display:flex;align-items:center;gap:8px;font-weight:700;font-size:11px;padding-left:10px}
.cup{width:16px;height:16px}
.vmenu{list-style:none;margin-top:9px}
.vmenu li{height:29px;padding-left:6px;font-size:10.5px;color:#333}
.pill{display:flex;align-items:center;justify-content:center;gap:8px;height:21px;margin-top:4px;border:2px solid var(--red);border-radius:7px;
  background:linear-gradient(#fff,#ddd);color:var(--red);font-weight:700;font-size:10.5px}
.search-box{height:15px;margin:4px 0 8px 2px;border:1px solid #999;background:#fff;position:relative}
.search-box svg{position:absolute;right:2px;top:1px}
.cat-intro{margin:5px 0 3px 6px;font-size:10px}
.cat-list{list-style:none;margin-left:8px}
.cat-list li{font-size:10.5px;height:15px;padding-left:12px;position:relative}
.cat-list li::before{content:"";position:absolute;left:0;top:4px;width:5px;height:5px;border:1.5px solid var(--visited);border-radius:50%}
.cat-list a{color:var(--visited)}
.content{position:absolute;left:168px;top:18px;width:490px}
.post-title{font-family:"Crimson Text",serif;font-weight:600;font-size:16px;color:var(--ink)}
.post-title a{color:var(--red);text-decoration:none}
.post-title a.hover{text-decoration:underline}
.meta{display:flex;align-items:center;gap:5px;margin-top:2px;height:17px;border:1px solid var(--rule);background:#fff;font-style:italic;font-size:10px;color:#444;padding-left:4px}
.meta a{color:#444}
.ico{width:11px;height:11px;display:inline-block}
.body-row{display:flex;margin-top:18px;padding-left:8px}
.photo{width:237px;height:172px;flex:none;background:linear-gradient(135deg,#6b6a70,#4a4250 50%,#2f3644);border:1px solid #999}
.text-col{margin-left:8px;font-size:10.5px;line-height:1.02}
.wrap-row{display:flex;gap:8px}
.badge{width:42px;height:44px;flex:none;border:1px solid #aaa;background:#fff;display:flex;align-items:center;justify-content:center}
.badge span{width:32px;height:32px;border-radius:50%;background:#2f6e9e}
.text-col p+p{margin-top:10px}
.text-col a{color:var(--link);text-decoration:none}
.text-col a.visited{color:var(--visited)}
.text-col a.hover{text-decoration:underline;color:var(--red-dark)}
sup,sub{font-size:7px}
.full{margin-top:14px;font-size:10.5px;line-height:1.02}
.foot{display:flex;align-items:center;gap:5px;margin-top:10px;font-style:italic;font-size:10px;color:#444}
.foot a{color:#444}
.foot .hov{color:var(--red);text-decoration:none}
.post-2{margin-top:25px}
.heading{font-family:"Crimson Text",serif;font-weight:600;font-size:20px;margin-top:6px;color:#333}
</style>
</head>
<body>
<div class="top-strip" role="img" aria-label="Roasted coffee bean texture"></div>
<nav class="main-nav"><a>Home</a><a>Menu Item</a><a>About</a></nav>
<header class="site-header">
  <div class="brand"><span class="brand-dot"></span><span class="brand-name">Mug Rover</span></div>
</header>
<div class="bean-backdrop" role="img" aria-label="Close-up of roasted coffee beans"></div>

<main class="page">
  <aside class="sidebar">
    <div class="widget-title"><svg class="cup" viewBox="0 0 16 16"><path d="M2 7h10v4a4 4 0 0 1-4 4H6a4 4 0 0 1-4-4z" fill="#7a1a14"/><path d="M12 8h1.5a1.5 1.5 0 0 1 0 3H12" fill="none" stroke="#7a1a14"/><path d="M5 5c0-2 2-2 2-4M8 5c0-2 2-2 2-4" stroke="#b08060" fill="none"/></svg>Vertical Menu</div>
    <ul class="vmenu"><li>Item</li><li>News</li><li>Video</li><li>Archive</li><li>Forum</li><li>About</li><li>Contact</li></ul>
    <div class="pill"><svg class="cup" viewBox="0 0 16 16"><path d="M2 7h10v4a4 4 0 0 1-4 4H6a4 4 0 0 1-4-4z" fill="#7a1a14"/></svg>Search</div>
    <div class="search-box"><svg width="11" height="11" viewBox="0 0 11 11"><circle cx="4.5" cy="4.5" r="3.3" fill="none" stroke="#666"/><path d="M7 7l3 3" stroke="#666" stroke-width="1.5"/></svg></div>
    <div class="pill"><svg class="cup" viewBox="0 0 16 16"><path d="M2 7h10v4a4 4 0 0 1-4 4H6a4 4 0 0 1-4-4z" fill="#7a1a14"/></svg>Categories</div>
    <p class="cat-intro">Lorem ipsum dolor sit amet. Nam sit amet sem. Mauris a ante.</p>
    <ul class="cat-list">
      <li><a>All News</a> (50)</li>
      <li><a>Best of the Year</a> (4)</li>
      <li><a>Hyperlink</a> (24)</li>
    </ul>
  </aside>

  <section class="content">
    <article>
      <h2 class="post-title">Text, <a>Link</a>, Visited, <a class="hover">Hovered</a></h2>
      <div class="meta">
        <svg class="ico" viewBox="0 0 11 11"><rect x="1" y="1" width="9" height="9" fill="#fff" stroke="#a33"/><path d="M1 3h9" stroke="#a33"/></svg>
        Published November 05, 2008 | 
        <svg class="ico" viewBox="0 0 11 11"><circle cx="5.5" cy="3.5" r="2.5" fill="#555"/><path d="M1 11a4.5 4 0 0 1 9 0z" fill="#555"/></svg>
        By <a>admin</a> | 
        <svg class="ico" viewBox="0 0 11 11"><path d="M2 9l1-3 5-5 2 2-5 5z" fill="#c9a227" stroke="#555" stroke-width=".6"/></svg>
        <a>Edit</a>
      </div>
      <div class="body-row">
        <div class="photo" role="img" aria-label="Photo of a smiling young man sitting with friends"></div>
        <div class="text-col">
          <div class="wrap-row">
            <div class="badge"><span></span></div>
            <p>Lorem <sup>superscript</sup> dolor <sub>subscript</sub> amet, consectetuer adipiscing <a>link</a>, <a class="visited">visited link</a>, <a class="hover">hovered link</a> consectetuer adipiscing elit. Quisque sed felis. Aliquam sit amet felis. Mauris semper,</p>
          </div>
          <p style="margin-top:0">velit semper laoreet dictum, quam diam dictum urna, nec placerat elit nisl <a>one more link</a> in quam. Etiam augue pede, molestie eget, rhoncus at, convallis ut, eros.</p>
          <p>Aliquam pharetra. Nulla in tellus eget odio sagittis blandit.Maecenas at nisl. Nullam lorem mi, eleifend a, fringilla vel, semper at, ligula. Mauris eu wisi. Ut ante dui, aliquet nec, congue non, accumsan sit amet, lectus. Mauris et mauris. Duis sed massa id mauris pretium venenatis. Suspendisse cursus velit vel ligula. Mauris elit.</p>
        </div>
      </div>
      <p class="full">Aliquam pharetra. Nulla in tellus eget odio sagittis blandit.Maecenas at nisl. Nullam lorem mi, eleifend a, fringilla vel, semper at, ligula. Mauris eu wisi. Ut ante dui, aliquet nec, congue non, accumsan sit amet, lectus. Mauris et mauris. Duis sed massa id mauris pretium venenatis. Suspendisse cursus velit vel ligula. Mauris elit.</p>
      <div class="foot">
        <svg class="ico" viewBox="0 0 11 11"><path d="M0 2h4l1 1h6v7H0z" fill="#b3141a"/></svg>
        Category: No Category | 
        <svg class="ico" viewBox="0 0 11 11"><path d="M1 3h6l3 2.5-3 2.5H1z" fill="none" stroke="#b3141a"/></svg>
        Tags: <a>link</a>, <a>visited</a>, <a class="hov">hovered</a> | 
        <svg class="ico" viewBox="0 0 11 11"><rect x="0.5" y="1" width="10" height="7" rx="1" fill="#e88" stroke="#a33"/><path d="M3 8v3l3-3" fill="#a33"/></svg>
        <a>No Comments »</a>
      </div>
    </article>
    <article class="post-2">
      <h2 class="post-title"><a>Worth A Thousand Words</a></h2>
      <div class="meta">
        <svg class="ico" viewBox="0 0 11 11"><rect x="1" y="1" width="9" height="9" fill="#fff" stroke="#a33"/><path d="M1 3h9" stroke="#a33"/></svg>
        Published September 11, 2008 | 
        <svg class="ico" viewBox="0 0 11 11"><circle cx="5.5" cy="3.5" r="2.5" fill="#555"/><path d="M1 11a4.5 4 0 0 1 9 0z" fill="#555"/></svg>
        By <a>admin</a> | 
        <svg class="ico" viewBox="0 0 11 11"><path d="M2 9l1-3 5-5 2 2-5 5z" fill="#c9a227" stroke="#555" stroke-width=".6"/></svg>
        <a>Edit</a>
      </div>
      <h3 class="heading">Heading 1</h3>
    </article>
  </section>
</main>
</body>
</html>
```